Business Card Design Competition

We need a business card design for our Internet Marketing company. We require both front and back designs and the final card must be 89x53mm in size, plus crop marks to 91x55mm. Colours as per logo, plus perhaps black and/or grey (#828282).
Final text must be editable (if you can supply an editable Fireworks PNG, even better)...
FRONT TEXT:
Full Name
Position
Address Line
Suburb, State, Postcode
Phone: 0000 000 000
Mobile: 0000 000 000
Email: xxx@brimleafpromo.com.au
Web: www.brimleafpromo.com.au
Rear of card should be a fresh design plus our slogan text: "Getting You Noticed" in large font, then in small text "Brimleaf Holdings Pty Ltd (ABN: 42 563 701 384)".
Target Market(s)
Small/Medium Businesses
Industry/Entity Type
Business
Look and feel
Each slider illustrates characteristics of the customer's brand and the style your logo design should communicate.

```html
<!DOCTYPE html>
<html lang="en">
<head>
<meta charset="utf-8">
<title>Brimleaf Promo – Business Card</title>
<link href="https://fonts.googleapis.com/css2?family=Cinzel:wght@400;500&family=Exo+2:wght@400&family=Montserrat:wght@300;400;600&display=swap" rel="stylesheet">
<style>
  :root {
    --orange: #f7a12a;
    --green: #8cc63f;
    --ink: #2b2b2b;
    --grey: #828282;
    --band: #666666;
    --white: #ffffff;
  }
  html, body { margin: 0; padding: 0; overflow: hidden; }
  body {
    width: 1200px; height: 1200px; position: relative;
    background: linear-gradient(#c9c9c9 0%, #8a8a8a 50%, #a9a9a9 100%);
    font-family: "Montserrat", sans-serif;
  }
  .card { position: absolute; overflow: hidden; box-shadow: 0 6px 14px rgba(0,0,0,.55); }

  /* Rear: slogan side */
  .card-rear {
    left: 193px; top: 65px; width: 828px; height: 492px;
    background: radial-gradient(ellipse 70% 60% at 50% 28%, #6a6a6a 0%, #3e3e3e 60%, #2a2a2a 100%);
  }
  .card-rear svg { position: absolute; left: 0; top: 0; }
  .rear-name {
    position: absolute; left: 340px; top: 180px;
    font-family: "Exo 2", sans-serif; font-size: 62px; line-height: 1;
    color: var(--orange);
  }
  .slogan {
    position: absolute; left: 343px; top: 314px;
    font-family: "Exo 2", sans-serif; font-size: 38px; color: var(--white);
    letter-spacing: .5px;
  }
  .legal {
    position: absolute; right: 8px; bottom: 4px;
    font-size: 15px; color: #e8e8e8;
  }

  /* Front: contact side */
  .card-front {
    left: 195px; top: 641px; width: 826px; height: 492px;
    background: linear-gradient(#bdbdbd 0%, #f4f4f4 16%, #ffffff 30%, #ffffff 100%);
  }
  .person { position: absolute; left: 380px; top: 38px; width: 340px; text-align: center; }
  .person-name {
    font-family: "Cinzel", serif; font-size: 54px; font-weight: 500; color: var(--ink);
    line-height: 1; white-space: nowrap; margin-left: -10px;
  }
  .person-rule { height: 3px; width: 248px; margin: 8px auto 0; background: var(--ink); border-radius: 2px; }
  .person-title {
    font-family: "Cinzel", serif; font-size: 20px; color: var(--ink);
    margin-top: 6px; letter-spacing: .5px;
  }
  .contacts { position: absolute; left: 33px; top: 192px; margin: 0; }
  .contacts dt { color: var(--green); font-weight: 600; font-size: 12px; line-height: 12px; }
  .contacts dd { margin: 0 0 5px; color: #333; font-size: 22px; font-weight: 400; line-height: 23px; }
  .web-band {
    position: absolute; left: 0; top: 371px; width: 826px; height: 72px;
    background: var(--band);
    border-top: 2px solid #e5e5e5; border-bottom: 2px solid #e5e5e5;
    box-shadow: 0 0 0 2px #888;
  }
  .web-url {
    position: absolute; left: 18px; top: 382px;
    font-size: 30px; font-weight: 400; color: var(--white); letter-spacing: 1px;
  }
  .card-front svg { position: absolute; left: 510px; top: 352px; }
  .front-name {
    position: absolute; left: 612px; top: 390px;
    font-family: "Exo 2", sans-serif; font-size: 28px; color: var(--orange); white-space: nowrap;
  }
</style>
</head>
<body>

<section class="card card-rear" aria-label="Card rear">
  <svg width="828" height="492" viewBox="0 0 828 492" aria-hidden="true">
    <rect class="slogan-band" x="300" y="175" width="528" height="135" fill="#ffffff"/>
    <circle class="brand-dot" cx="217" cy="238" r="115" fill="#ffffff"/>
  </svg>
  <div class="rear-name">Brimleaf Promo</div>
  <div class="slogan">Getting You Noticed</div>
  <div class="legal">Brimleaf Holdings Pty Ltd (ABN: 42 563 701 384)</div>
</section>

<section class="card card-front" aria-label="Card front">
  <div class="person">
    <div class="person-name">Daniel Harrow</div>
    <div class="person-rule"></div>
    <div class="person-title">Internet Marketer</div>
  </div>
  <dl class="contacts">
    <dt>a.</dt><dd>14 Wattle Lane, State, AB-22</dd>
    <dt>p.</dt><dd>0000 000 000</dd>
    <dt>m.</dt><dd>0000 000 000</dd>
    <dt>e.</dt><dd>dharrow@brimleafpromo.com.au</dd>
  </dl>
  <div class="web-band"></div>
  <div class="web-url">www.brimleafpromo.com.au</div>
  <svg width="100" height="100" viewBox="0 0 100 100" aria-hidden="true">
    <circle cx="50" cy="50" r="47" fill="#555555" stroke="#e8e8e8" stroke-width="3"/>
  </svg>
  <div class="front-name">Brimleaf Promo</div>
</section>

</body>
</html>
```